Computer Training in the Education sector - Letterhead

We need a new letter head to be designed for the company. We provide computer training fro the Education Sector, both primary and private tertiary providers. The colours will need to tie in with the website www.lanternpathlearning.co.nz.
The company name is Lantern Path Co with the tag line of Computer Training for Educators.
The footer will need to have the following detail...
0508 KEY MENTOR
027 813 459
www.lanternpathlearning.co.nz / lessons@lanternpathlearning.co.nz
Updates

Thanks for the designs so far.

Some have watermarks in the background. Please don't worry about using watermarks as I will not be using a watermark in in a final design.
Regards,
Morris

Thank you for all the designs and the effort. There was some great concepts that came through.

Cheers
Morris

Industry/Entity Type

Computer

```html
<!DOCTYPE html>
<html lang="en">
<head>
<meta charset="utf-8">
<title>Lantern Path Co – Letterhead</title>
<link rel="stylesheet" href="https://fonts.googleapis.com/css2?family=Open+Sans:wght@400;600&display=swap">
<style>
  :root {
    --paper: #ffffff;
    --brand-blue: #2f7fd8;
    --rule-blue: #2b78d6;
    --leaf-green: #8ed62c;
    --warm-orange: #ef8a2e;
    --sky-blue: #3a86e0;
  }
  html, body {
    margin: 0;
    padding: 0;
    width: 848px;
    height: 1200px;
    overflow: hidden;
    background: var(--paper);
  }
  .letterhead {
    position: relative;
    width: 848px;
    height: 1200px;
    background: var(--paper);
    font-family: "Open Sans", Verdana, sans-serif;
    color: var(--brand-blue);
  }
  .brand-name {
    position: absolute;
    left: 54px;
    top: 34px;
    margin: 0;
    width: 150px;
    font-size: 30px;
    line-height: 36px;
    font-weight: 400;
    color: var(--brand-blue);
  }
  .contact-list {
    position: absolute;
    left: 206px;
    top: 36px;
    margin: 0;
    padding: 0;
    list-style: none;
    font-size: 15.5px;
    letter-spacing: 0.6px;
    color: var(--brand-blue);
  }
  .contact-list li { position: absolute; left: 0; white-space: nowrap; }
  .contact-list .phone-free { top: 0; }
  .contact-list .phone-mobile { top: 24px; }
  .contact-list .email { top: 55px; }
  .contact-list .web { top: 84px; }
  .header-rule {
    position: absolute;
    left: 25px;
    top: 172px;
    width: 801px;
    height: 4px;
    background: var(--rule-blue);
  }
  .footer-art {
    position: absolute;
    left: 0;
    bottom: 0;
    width: 848px;
    height: 200px;
  }
</style>
</head>
<body>
  <div class="letterhead">
    <header>
      <p class="brand-name">Lantern Path Co</p>
      <ul class="contact-list">
        <li class="phone-free">0508 KEY MENTOR</li>
        <li class="phone-mobile">027 813 459</li>
        <li class="email">lessons@lanternpathlearning.co.nz</li>
        <li class="web">www.lanternpathlearning.co.nz</li>
      </ul>
      <div class="header-rule"></div>
    </header>

    <svg class="footer-art" role="img" aria-label="Decorative footer of green, orange and blue tile ribbons sweeping across the page bottom" viewBox="0 0 848 200" preserveAspectRatio="none">
      <defs>
        <linearGradient id="footer-tones" x1="0" y1="0" x2="1" y2="0">
          <stop offset="0" stop-color="#8ed62c"/>
          <stop offset="0.3" stop-color="#ef8a2e"/>
          <stop offset="0.55" stop-color="#3a86e0"/>
          <stop offset="1" stop-color="#8ed62c"/>
        </linearGradient>
        <linearGradient id="footer-fade" x1="0" y1="0" x2="0" y2="1">
          <stop offset="0" stop-color="#fff" stop-opacity="1"/>
          <stop offset="0.55" stop-color="#fff" stop-opacity="0.35"/>
          <stop offset="1" stop-color="#fff" stop-opacity="0"/>
        </linearGradient>
      </defs>
      <rect width="848" height="200" fill="url(#footer-tones)" opacity="0.75"/>
      <rect width="848" height="200" fill="url(#footer-fade)"/>
    </svg>
  </div>
</body>
</html>
```